Steel Company / Iron Railing Business Card Template

We are a custom steel fabrication company located in Harlow Mill, PA. In business since 1979, we recently developed a new logo, and we're looking for a business card design to help display the new logo and our business. The name of the company is Kelbrook Forge Co.. The Office Phone number is (610) 555-0143. We fabricate and install custom "wrought iron" railings on our residential side, we also fabricate and erect structural steel (think cranes and steel beams in buildings) on our commercial side. Looking to get a business card template designed. Something modern, but professional. Clear and easy to read. Front should have all business and employee information including phone number(s), email address, business information, etc. back should spotlight logo.

Industry/Entity Type

Construction / Home Improvement

Contact Information for Business Card

Business information is Kelbrook Forge Co., 48 Dunmore Ave Suite 3305, Harlow Mill, PA 19074. Phone number is (610) 555-0143. Website is www.kelbrookforge.example Business card should be for "Tom Pelling" with the job title "Sales & Estimating" but be editable for other employees. Tom's phone number is (610) 555-0178

Colors

Designer to choose colors to be used in the design.

Requirements
Must have
• Modern Feel, Design should be sized for standard business card sizing 3.5" x 2" (88.9mm x 50.8mm)

```html
<!DOCTYPE html>
<html lang="en">
<head>
<meta charset="utf-8">
<title>Kelbrook Forge Co. – Business Card</title>
<link rel="stylesheet" href="https://fonts.googleapis.com/css2?family=Montserrat:wght@400;500;700&display=swap">
<style>
  :root {
    --page-bg: #d8d1c6;
    --card-bg: #efebe4;
    --card-edge: #f7f4ee;
    --ink-navy: #1f3566;
    --ink-body: #3a3a3a;
  }
  * { margin: 0; padding: 0; box-sizing: border-box; }
  html, body {
    width: 1200px;
    height: 1047px;
    overflow: hidden;
    background: var(--page-bg);
    font-family: "Montserrat", sans-serif;
  }
  .business-card {
    position: absolute;
    left: 151px;
    top: 289px;
    width: 947px;
    height: 518px;
    background: var(--card-bg);
    border: 2px solid var(--card-edge);
    border-radius: 26px;
    box-shadow: 0 10px 30px rgba(60, 50, 40, 0.18);
  }
  .brand-mark {
    position: absolute;
    left: 111px;
    top: 173px;
    width: 360px;
    height: 170px;
    display: flex;
    flex-direction: column;
    align-items: center;
    justify-content: center;
    color: var(--ink-navy);
    font-weight: 700;
    font-size: 46px;
    line-height: 1.15;
    text-align: center;
    letter-spacing: 0.5px;
  }
  .divider {
    position: absolute;
    left: 508px;
    top: 119px;
    width: 3px;
    height: 280px;
    background: var(--ink-navy);
  }
  .contact-line {
    position: absolute;
    left: 545px;
    white-space: nowrap;
    color: var(--ink-body);
    font-size: 24px;
    line-height: 36px;
  }
  .employee-name {
    top: 115px;
    font-weight: 700;
    font-size: 38px;
    line-height: 42px;
    color: var(--ink-navy);
  }
  .employee-title { top: 160px; font-size: 23px; }
  .address-street { top: 212px; }
  .address-town   { top: 248px; }
  .mobile-line    { top: 297px; }
  .office-line    { top: 333px; }
  .web-line       { top: 369px; }
  .with-icon {
    display: flex;
    align-items: center;
    gap: 12px;
  }
  .contact-icon {
    width: 20px;
    height: 20px;
    fill: var(--ink-navy);
    flex-shrink: 0;
  }
</style>
</head>
<body>
  <div class="business-card">
    <div class="brand-mark">
      <span>Kelbrook</span>
      <span>Forge Co.</span>
    </div>

    <div class="divider"></div>

    <div class="contact-line employee-name">Tom Pelling</div>
    <div class="contact-line employee-title">Sales &amp; Estimating</div>
    <div class="contact-line address-street">48 Dunmore Ave Suite 3305</div>
    <div class="contact-line address-town">Harlow Mill, PA 19074</div>

    <div class="contact-line mobile-line with-icon">
      <svg class="contact-icon" viewBox="0 0 20 20" aria-hidden="true">
        <path d="M6 1h8a1.5 1.5 0 0 1 1.5 1.5v15A1.5 1.5 0 0 1 14 19H6a1.5 1.5 0 0 1-1.5-1.5v-15A1.5 1.5 0 0 1 6 1zm0 2v12h8V3H6zm4 13a1 1 0 1 0 0 2 1 1 0 0 0 0-2z"/>
      </svg>
      (610) 555-0178
    </div>
    <div class="contact-line office-line with-icon">
      <svg class="contact-icon" viewBox="0 0 20 20" aria-hidden="true">
        <path d="M2 7c0-2 3.5-4 8-4s8 2 8 4v1.5h-4V7c-1-0.6-2.4-0.9-4-0.9S7 6.4 6 7v1.5H2V7z"/>
        <path d="M5 10h10l2 7H3l2-7zm5 1.8a2 2 0 1 0 0 4 2 2 0 0 0 0-4z"/>
      </svg>
      (610) 555-0143
    </div>
    <div class="contact-line web-line with-icon">
      <svg class="contact-icon" viewBox="0 0 20 20" aria-hidden="true">
        <circle cx="10" cy="10" r="8.5"/>
        <path d="M10 1.5v17M1.5 10h17M4 4.5c3.5 2 8.5 2 12 0M4 15.5c3.5-2 8.5-2 12 0" stroke="#efebe4" stroke-width="1.3" fill="none"/>
      </svg>
      www.kelbrookforge.example
    </div>
  </div>
</body>
</html>
```